Social News web page design website name Velnu.

I need a web design for a start up project called Velnu based in Sydney. Its a social news website. it helps people to get centralized news and people can have their own profiles where they can post there thoughts and comments and it will be free to signup and usage as well.

I would like to see designs that use the latest murlan bootstrap framework and are mobile compatible. only need 2 pages a home page kind of similar to
plom (http://plom.example/) and a profile that's a next gen user profile page I will leave that to you imaginations

this is my previous design I did on my own http://www.velnu-site.example/

Target Market(s)

target market is 13 and up and anyone who likes or uses social media and would be able to understand the site

Industry/Entity Type

News

Requirements
Must have
• 1.) using murlan bootstrap. 2) a home page similar to plom (http://plom.example/) or even better free to use your imagination 3) a next gen profile page better the one i made on my own which is this one (http://www.velnu-site.example/profile/korelatimbo) 4) for mobile navigation, have a mobile navigation something similar to http://zanpel.wovrite.example/
Nice to have
• 1) a sexy navigation and layout for both desktop and mobile phones. i will leave that to you imaginations. 2) social medial buttons like to sign-in with and also to post a story to Linkora or murlan 3) a user settings page (but not necessary) 4) a login or signup (but not necessary)

```html
<!DOCTYPE html>
<html lang="en">
<head>
<meta charset="utf-8">
<title>Velnu – Social news website</title>
<link href="https://fonts.googleapis.com/css2?family=Abel&display=swap" rel="stylesheet">
<style>
:root{
  --header:#438f9f;
  --teal:#149c9c;
  --teal-text:#1a9fa5;
  --page:#efefef;
  --card:#ffffff;
  --ink:#222;
  --muted:#888;
  --rule:#e6e6e6;
  --footer:#585858;
  --footer-text:#e2e2e2;
}
*{margin:0;padding:0;box-sizing:border-box}
html,body{width:897px;height:1200px;overflow:hidden}
body{position:relative;background:var(--page);font-family:"Abel",sans-serif;color:var(--ink)}

.site-header{position:absolute;left:0;top:0;width:897px;height:52px;background:var(--header)}
.brand{position:absolute;left:150px;top:12px;font-size:22px;color:#1c2b30;letter-spacing:.5px}
.main-nav{position:absolute;left:288px;top:18px;display:flex;gap:10px;font-size:10px;color:#fff}
.search{position:absolute;left:570px;top:15px;width:100px;height:14px;border-bottom:1px solid #cfe3e8}
.search svg{position:absolute;right:1px;top:1px}
.account{position:absolute;left:683px;top:19px;display:flex;gap:8px;font-size:8px;color:#fff}

.hero{position:absolute;left:0;top:52px;width:897px;height:228px;
  background:linear-gradient(90deg,#c9c2bb 0%,#e4ddd5 30%,#dcdcdc 60%,#ececec 100%)}
.hero-title{position:absolute;left:0;width:897px;text-align:center;top:75px;font-size:46px;line-height:1;color:#111}
.hero-sub{position:absolute;left:0;width:897px;text-align:center;top:123px;font-size:48px;line-height:1;color:#3aa3b2}

.filters{position:absolute;left:144px;top:305px;font-size:10px;color:#111}
.select{position:absolute;left:279px;top:305px;width:152px;height:15px;background:#fff;border:1px solid #e2e2e2}
.select::after{content:"";position:absolute;right:5px;top:5px;border:3px solid transparent;border-top:4px solid #999}
.tabs{position:absolute;left:594px;top:303px;display:flex;gap:3px;font-size:9px}
.tab{height:19px;display:flex;align-items:center;gap:5px;padding:0 8px}
.tab-trends{width:92px;background:#fff;color:var(--teal-text)}
.tab-popular{width:90px;background:var(--teal);color:#fff}

.story-grid{position:absolute;left:139px;top:356px;display:grid;grid-template-columns:repeat(3,197px);column-gap:24px;row-gap:18px}
.story{width:197px;height:217px;background:var(--card);border-top:7px solid var(--teal);box-shadow:0 1px 2px rgba(0,0,0,.08);position:relative}
.story-media{height:93px}
.story-title{font-size:11px;line-height:12px;color:var(--teal-text);padding:9px 10px 0}
.story-source{font-size:8.5px;padding:6px 10px 0}
.story-text{font-size:8px;line-height:11.5px;color:var(--muted);padding:1px 10px 0}
.story-actions{position:absolute;left:0;bottom:0;width:100%;height:25px;border-top:1px solid var(--rule);display:flex;align-items:center;font-size:8.5px;color:var(--teal-text)}
.share{position:absolute;left:26px;display:flex;align-items:center;gap:6px}
.vote{position:absolute;left:120px;display:flex;align-items:center;gap:4px}

.media-sport{background:linear-gradient(135deg,#2f4c78,#7a4a55 55,#39527d)}
.media-sport{background:linear-gradient(135deg,#2f4c78 0%,#a3444a 50%,#34507a 100%)}
.media-portrait{background:linear-gradient(135deg,#efe9e2,#cbb2a0)}
.media-grad{background:linear-gradient(135deg,#6f8391,#3f4650 50%,#c7ccd2)}
.media-stage{background:linear-gradient(135deg,#1f3f86,#9a7f6d 50%,#2a4a92)}

.loader{position:absolute;left:428px;top:1082px}
.site-footer{position:absolute;left:2px;top:1158px;width:895px;height:42px;background:var(--footer);color:var(--footer-text);font-size:10.5px;text-align:center;line-height:42px}
</style>
</head>
<body>
<header class="site-header">
  <div class="brand">Velnu</div>
  <nav class="main-nav"><span>Home</span><span>Pomo</span><span>Andrix</span><span>murlan</span><span>Linkora</span><span>The daily Velnu</span></nav>
  <div class="search"><svg width="11" height="11" viewBox="0 0 11 11"><circle cx="4.5" cy="4.5" r="3.3" fill="none" stroke="#1c2b30" stroke-width="1.6"/><line x1="7" y1="7" x2="10" y2="10" stroke="#1c2b30" stroke-width="1.8"/></svg></div>
  <div class="account"><span>SIGN IN</span><span>SIGN UP</span></div>
</header>

<section class="hero" role="img" aria-label="Photo of a smiling woman reading a newspaper with a coffee mug">
  <h1 class="hero-title">WELCOME</h1>
  <p class="hero-sub">Social news website</p>
</section>

<div class="filters">Choose Your Prefered County:</div>
<div class="select"></div>
<div class="tabs">
  <div class="tab tab-trends"><svg width="10" height="10" viewBox="0 0 10 10"><circle cx="5" cy="5" r="4.5" fill="#9aa"/></svg>Internet Trends</div>
  <div class="tab tab-popular"><svg width="10" height="10" viewBox="0 0 10 10"><rect x=".5" y=".5" width="9" height="9" fill="none" stroke="#fff"/><line x1="5" y1="0" x2="5" y2="10" stroke="#fff"/><line x1="0" y1="5" x2="10" y2="5" stroke="#fff"/></svg>Papular Stories</div>
</div>

<main class="story-grid">
  <article class="story"><div class="story-media media-sport" role="img" aria-label="Football player in red uniform helped off the field"></div><h2 class="story-title">Dario Kemble Injury: Updates on Harbormen LB's Leg and Return</h2><p class="story-source">sportsledger.example</p><p class="story-text">Bay City Harbormen linebacker Dario Kemble suffered a scary injury in the NCC Championship Game against the Coastline Gulls</p><div class="story-actions"><span class="share"><svg width="14" height="11" viewBox="0 0 14 11"><path d="M1 3v7h9V7" fill="none" stroke="#1a9fa5" stroke-width="1.6"/><path d="M5 7c1-3 3-4 6-4V1l3 3-3 3V5c-2 0-4 .5-6 2z" fill="#1a9fa5"/></svg>Shere Story</span><span class="vote">Vote &nbsp;( <svg width="9" height="10" viewBox="0 0 9 10"><path d="M1 4h2v6H1zM3.5 4L5 0c1 0 1.5.5 1.3 2L6 4h2.5v2L7 10H3.5z" fill="#1a9fa5"/></svg> 0 )</span></div></article>
  <article class="story"><div class="story-media media-portrait" role="img" aria-label="Portrait of an older man wearing thick glasses"></div><h2 class="story-title">Dario Kemble Injury: Updates on Harbormen LB's Leg and Return</h2><p class="story-source">sportsledger.example</p><p class="story-text">Bay City Harbormen linebacker Dario Kemble suffered a scary injury in the NCC Championship Game against the Coastline Gulls</p><div class="story-actions"><span class="share"><svg width="14" height="11" viewBox="0 0 14 11"><path d="M1 3v7h9V7" fill="none" stroke="#1a9fa5" stroke-width="1.6"/><path d="M5 7c1-3 3-4 6-4V1l3 3-3 3V5c-2 0-4 .5-6 2z" fill="#1a9fa5"/></svg>Shere Story</span><span class="vote">Vote &nbsp;( <svg width="9" height="10" viewBox="0 0 9 10"><path d="M1 4h2v6H1zM3.5 4L5 0c1 0 1.5.5 1.3 2L6 4h2.5v2L7 10H3.5z" fill="#1a9fa5"/></svg> 0 )</span></div></article>
  <article class="story"><div class="story-media media-grad" role="img" aria-label="Graduates in caps and gowns outdoors"></div><h2 class="story-title">Dario Kemble Injury: Updates on Harbormen LB's Leg and Return</h2><p class="story-source">sportsledger.example</p><p class="story-text">Bay City Harbormen linebacker Dario Kemble suffered a scary injury in the NCC Championship Game against the Coastline Gulls</p><div class="story-actions"><span class="share"><svg width="14" height="11" viewBox="0 0 14 11"><path d="M1 3v7h9V7" fill="none" stroke="#1a9fa5" stroke-width="1.6"/><path d="M5 7c1-3 3-4 6-4V1l3 3-3 3V5c-2 0-4 .5-6 2z" fill="#1a9fa5"/></svg>Shere Story</span><span class="vote">Vote &nbsp;( <svg width="9" height="10" viewBox="0 0 9 10"><path d="M1 4h2v6H1zM3.5 4L5 0c1 0 1.5.5 1.3 2L6 4h2.5v2L7 10H3.5z" fill="#1a9fa5"/></svg> 0 )</span></div></article>
  <article class="story"><div class="story-media media-stage" role="img" aria-label="Portrait of a man in front of stage lights"></div><h2 class="story-title">Dario Kemble Injury: Updates on Harbormen LB's Leg and Return</h2><p class="story-source">sportsledger.example</p><p class="story-text">Bay City Harbormen linebacker Dario Kemble suffered a scary injury in the NCC Championship Game against the Coastline Gulls</p><div class="story-actions"><span class="share"><svg width="14" height="11" viewBox="0 0 14 11"><path d="M1 3v7h9V7" fill="none" stroke="#1a9fa5" stroke-width="1.6"/><path d="M5 7c1-3 3-4 6-4V1l3 3-3 3V5c-2 0-4 .5-6 2z" fill="#1a9fa5"/></svg>Shere Story</span><span class="vote">Vote &nbsp;( <svg width="9" height="10" viewBox="0 0 9 10"><path d="M1 4h2v6H1zM3.5 4L5 0c1 0 1.5.5 1.3 2L6 4h2.5v2L7 10H3.5z" fill="#1a9fa5"/></svg> 0 )</span></div></article>
  <article class="story"><div class="story-media media-grad" role="img" aria-label="Graduates in caps and gowns outdoors"></div><h2 class="story-title">Dario Kemble Injury: Updates on Harbormen LB's Leg and Return</h2><p class="story-source">sportsledger.example</p><p class="story-text">Bay City Harbormen linebacker Dario Kemble suffered a scary injury in the NCC Championship Game against the Coastline Gulls</p><div class="story-actions"><span class="share"><svg width="14" height="11" viewBox="0 0 14 11"><path d="M1 3v7h9V7" fill="none" stroke="#1a9fa5" stroke-width="1.6"/><path d="M5 7c1-3 3-4 6-4V1l3 3-3 3V5c-2 0-4 .5-6 2z" fill="#1a9fa5"/></svg>Shere Story</span><span class="vote">Vote &nbsp;( <svg width="9" height="10" viewBox="0 0 9 10"><path d="M1 4h2v6H1zM3.5 4L5 0c1 0 1.5.5 1.3 2L6 4h2.5v2L7 10H3.5z" fill="#1a9fa5"/></svg> 0 )</span></div></article>
  <article class="story"><div class="story-media media-sport" role="img" aria-label="Football player in red uniform helped off the field"></div><h2 class="story-title">Dario Kemble Injury: Updates on Harbormen LB's Leg and Return</h2><p class="story-source">sportsledger.example</p><p class="story-text">Bay City Harbormen linebacker Dario Kemble suffered a scary injury in the NCC Championship Game against the Coastline Gulls</p><div class="story-actions"><span class="share"><svg width="14" height="11" viewBox="0 0 14 11"><path d="M1 3v7h9V7" fill="none" stroke="#1a9fa5" stroke-width="1.6"/><path d="M5 7c1-3 3-4 6-4V1l3 3-3 3V5c-2 0-4 .5-6 2z" fill="#1a9fa5"/></svg>Shere Story</span><span class="vote">Vote &nbsp;( <svg width="9" height="10" viewBox="0 0 9 10"><path d="M1 4h2v6H1zM3.5 4L5 0c1 0 1.5.5 1.3 2L6 4h2.5v2L7 10H3.5z" fill="#1a9fa5"/></svg> 0 )</span></div></article>
  <article class="story"><div class="story-media media-portrait" role="img" aria-label="Portrait of an older man wearing thick glasses"></div><h2 class="story-title">Dario Kemble Injury: Updates on Harbormen LB's Leg and Return</h2><p class="story-source">sportsledger.example</p><p class="story-text">Bay City Harbormen linebacker Dario Kemble suffered a scary injury in the NCC Championship Game against the Coastline Gulls</p><div class="story-actions"><span class="share"><svg width="14" height="11" viewBox="0 0 14 11"><path d="M1 3v7h9V7" fill="none" stroke="#1a9fa5" stroke-width="1.6"/><path d="M5 7c1-3 3-4 6-4V1l3 3-3 3V5c-2 0-4 .5-6 2z" fill="#1a9fa5"/></svg>Shere Story</span><span class="vote">Vote &nbsp;( <svg width="9" height="10" viewBox="0 0 9 10"><path d="M1 4h2v6H1zM3.5 4L5 0c1 0 1.5.5 1.3 2L6 4h2.5v2L7 10H3.5z" fill="#1a9fa5"/></svg> 0 )</span></div></article>
  <article class="story"><div class="story-media media-stage" role="img" aria-label="Portrait of a man in front of stage lights"></div><h2 class="story-title">Dario Kemble Injury: Updates on Harbormen LB's Leg and Return</h2><p class="story-source">sportsledger.example</p><p class="story-text">Bay City Harbormen linebacker Dario Kemble suffered a scary injury in the NCC Championship Game against the Coastline Gulls</p><div class="story-actions"><span class="share"><svg width="14" height="11" viewBox="0 0 14 11"><path d="M1 3v7h9V7" fill="none" stroke="#1a9fa5" stroke-width="1.6"/><path d="M5 7c1-3 3-4 6-4V1l3 3-3 3V5c-2 0-4 .5-6 2z" fill="#1a9fa5"/></svg>Shere Story</span><span class="vote">Vote &nbsp;( <svg width="9" height="10" viewBox="0 0 9 10"><path d="M1 4h2v6H1zM3.5 4L5 0c1 0 1.5.5 1.3 2L6 4h2.5v2L7 10H3.5z" fill="#1a9fa5"/></svg> 0 )</span></div></article>
  <article class="story"><div class="story-media media-sport" role="img" aria-label="Football player in red uniform helped off the field"></div><h2 class="story-title">Dario Kemble Injury: Updates on Harbormen LB's Leg and Return</h2><p class="story-source">sportsledger.example</p><p class="story-text">Bay City Harbormen linebacker Dario Kemble suffered a scary injury in the NCC Championship Game against the Coastline Gulls</p><div class="story-actions"><span class="share"><svg width="14" height="11" viewBox="0 0 14 11"><path d="M1 3v7h9V7" fill="none" stroke="#1a9fa5" stroke-width="1.6"/><path d="M5 7c1-3 3-4 6-4V1l3 3-3 3V5c-2 0-4 .5-6 2z" fill="#1a9fa5"/></svg>Shere Story</span><span class="vote">Vote &nbsp;( <svg width="9" height="10" viewBox="0 0 9 10"><path d="M1 4h2v6H1zM3.5 4L5 0c1 0 1.5.5 1.3 2L6 4h2.5v2L7 10H3.5z" fill="#1a9fa5"/></svg> 0 )</span></div></article>
</main>

<svg class="loader" width="46" height="46" viewBox="0 0 46 46" aria-label="Loading more stories">
  <g fill="#333">
    <circle cx="23" cy="3" r="2" opacity=".3"/><circle cx="31" cy="4.6" r="2" opacity=".3"/><circle cx="37.1" cy="8.9" r="2" opacity=".3"/>
    <circle cx="41.4" cy="15" r="2.4" opacity=".5"/><circle cx="43" cy="23" r="2.6" opacity=".7"/><circle cx="41.4" cy="31" r="2.8"/>
    <circle cx="37.1" cy="37.1" r="2.8"/><circle cx="31" cy="41.4" r="2" opacity=".3"/><circle cx="23" cy="43" r="2" opacity=".3"/>
    <circle cx="15" cy="41.4" r="2" opacity=".4"/><circle cx="8.9" cy="37.1" r="2.6" opacity=".8"/><circle cx="4.6" cy="31" r="2.8"/>
    <circle cx="3" cy="23" r="2.8"/><circle cx="4.6" cy="15" r="2.6"/><circle cx="8.9" cy="8.9" r="2.2" opacity=".6"/><circle cx="15" cy="4.6" r="2" opacity=".3"/>
  </g>
</svg>

<footer class="site-footer">© 2014 - Velnu - home - about - contact - FAQ</footer>
</body>
</html>
```